Jägerbrief
Zielgruppe
Es soll ein 'Jägerbrief' werden. Diesen Jägerbrief erhält ein Jäger, wenn er sein erstes Stück Wild auf einer Jagd erlegen konnte.
Aufgabenstellung
Das Design ist im Format einer Urkunde auszuhändigen und sollte gerne in einem traditionellen Design gemacht werden. Beispielbilder sind im Anhang und können gerne als Inspiration genommen werden.
Genaue Details:
Überschrift in groß 'Jägerbrief'
Darunter den Text zentriert wie folgt abbilden:
'Im Revier von Tannwöhrden, gelegen im Herzen von Kleimarschen, tratst du,
zur Niederwildjagd an und bewiesest dein Können, deinen Respekt vor der Natur und deine Geduld im Angesicht der Herausforderung.
An diesem besonderen Tag hattest du die Ehre, deinen ersten Feldhasen zu strecken. Mit diesem Erfolg trittst du in die stolze Tradition der Waidmänner ein, die die Schönheit und den Wert unserer heimischen Wildbestände zu schätzen wissen und Verantwortung für deren Erhalt übernehmen.
Möge dieser Moment dir stets in Erinnerung bleiben und dir ein Ansporn sein, die Jagd mit Demut, Leidenschaft und Verantwortung auszuüben.
Mit diesem Jägerbrief gratulieren wir dir herzlich zu deinem ersten Feldhasen und wünschen dir weiterhin Waidmannsheil auf all deinen Wegen im Revier.
Hochachtungsvoll und mit Waidmannsgruß
Die Jagdgesellschaft von Tannwöhrden'

```html
<!DOCTYPE html>
<html lang="de">
<head>
<meta charset="utf-8">
<title>Jägerbrief</title>
<link rel="stylesheet" href="https://fonts.googleapis.com/css2?family=Cormorant+SC:wght@500&family=EB+Garamond:wght@400&display=swap">
<style>
  :root {
    --paper: #ffffff;
    --ink: #2b2b2b;
    --frame: #9a9a9a;
    --rule: #222222;
    --snow: #f4f6f7;
    --frost: #c9d1d4;
    --pine: #6f7b7d;
  }
  html, body {
    margin: 0;
    padding: 0;
    overflow: hidden;
    background: var(--paper);
  }
  .certificate {
    position: relative;
    width: 849px;
    height: 1200px;
    box-sizing: border-box;
    border: 1px solid var(--frame);
    background: var(--paper);
    overflow: hidden;
    color: var(--ink);
    font-family: "EB Garamond", Georgia, serif;
  }
  .certificate__title {
    position: absolute;
    top: 66px;
    left: 0;
    right: 0;
    margin: 0;
    text-align: center;
    font-family: "Cormorant SC", "EB Garamond", serif;
    font-weight: 500;
    font-size: 58px;
    letter-spacing: 1px;
    line-height: 1;
    color: var(--ink);
  }
  .certificate__text {
    position: absolute;
    left: 0;
    right: 0;
    margin: 0;
    text-align: center;
    font-size: 15.6px;
    line-height: 24.2px;
  }
  .certificate__intro { top: 158px; }
  .certificate__name-line {
    position: absolute;
    top: 275px;
    left: 228px;
    width: 403px;
    height: 0;
    border-top: 1.6px solid var(--rule);
  }
  .certificate__body { top: 300px; }
  .certificate__body p { margin: 0 0 22px; }
  .certificate__closing { top: 622px; }
  .certificate__closing p { margin: 0 0 21px; }
  .certificate__scene {
    position: absolute;
    left: 0;
    right: 0;
    bottom: 0;
    height: 540px;
    background:
      radial-gradient(ellipse 60% 45% at 50% 100%, var(--snow) 0%, transparent 70%),
      linear-gradient(to bottom, rgba(255,255,255,0) 0%, var(--frost) 38%, var(--pine) 62%, var(--frost) 82%, var(--snow) 100%);
    opacity: 0.75;
  }
</style>
</head>
<body>
  <main class="certificate">
    <h1 class="certificate__title">Jägerbrief</h1>

    <p class="certificate__text certificate__intro">
      Im Revier von Tannwöhrden, gelegen im Herzen von Kleimarschen, tratst du,
    </p>

    <div class="certificate__name-line"></div>

    <div class="certificate__text certificate__body">
      <p>zur Niederwildjagd an und bewiesest dein Können, deinen Respekt vor der Natur<br>
      und deine Geduld im Angesicht der Herausforderung.</p>
      <p>An diesem besonderen Tag hattest du die Ehre, deinen ersten Feldhasen zu strecken.<br>
      Mit diesem Erfolg trittst du in die stolze Tradition der Waidmänner ein, die die Schönheit<br>
      und den Wert unserer heimischen Wildbestände zu schätzen wissen und<br>
      Verantwortung für deren Erhalt übernehmen.</p>
      <p>Möge dieser Moment dir stets in Erinnerung bleiben und dir ein Ansporn sein,<br>
      die Jagd mit Demut, Leidenschaft und Verantwortung auszuüben.</p>
      <p>Mit diesem Jägerbrief gratulieren wir dir herzlich zu deinem ersten Feldhasen und<br>
      wünschen dir weiterhin Waidmannsheil auf all deinen Wegen im Revier.</p>
    </div>

    <div class="certificate__text certificate__closing">
      <p>Hochachtungsvoll und mit Waidmannsgruß</p>
      <p>Die Jagdgesellschaft von Tannwöhrden</p>
    </div>

    <div class="certificate__scene" role="img" aria-label="Aquarell einer verschneiten Winterlandschaft mit Tannen, einem stehenden Hirsch und einem sitzenden Feldhasen"></div>
  </main>
</body>
</html>
```